Business Card Design needed for start up company Pramora

In need of a new business card designed for a start up company based in Sydney, Pramora is a new start up innovative Company, our mission it to make property accessible for everyday Australian and to become the leading Real Estate platform in Australia. We want it to be fresh and clean.

Industry/Entity Type

Financial

Contact Information for Business Card

Section for Name
Section for Title

PRAMORA - Where Doors Open Wide
Mobile:
Direct:

Font styles to use
Sans Serif

Colors
33a6d7
0692cd
0255a3
ffffff

Requirements
Must have
• Logo, all business card details

```html
<!DOCTYPE html>
<html lang="en">
<head>
<meta charset="utf-8">
<title>Pramora Business Card</title>
<link rel="stylesheet" href="https://fonts.googleapis.com/css2?family=Source+Sans+3:wght@400;600;700&display=swap">
<style>
  :root {
    --backdrop: #2a2a2a;
    --card-white: #ffffff;
    --brand-navy: #1f3f7a;
    --brand-sky: #2a9bd8;
    --brand-sky-back: #2f9ad6;
    --brand-sky-soft: #4aaee0;
    --ink: #2b2b2b;
  }
  html, body {
    margin: 0;
    padding: 0;
    width: 1200px;
    height: 900px;
    overflow: hidden;
    background: var(--backdrop);
    font-family: "Source Sans 3", "Helvetica Neue", Arial, sans-serif;
  }
  .stage {
    position: relative;
    width: 1200px;
    height: 900px;
  }
  .card {
    position: absolute;
    top: 306px;
    width: 440px;
    height: 271px;
    overflow: hidden;
  }
  .card-front {
    left: 149px;
    background: var(--card-white);
  }
  .card-back {
    left: 608px;
    width: 441px;
  }
  .card-shapes {
    position: absolute;
    inset: 0;
  }
  .holder-name {
    position: absolute;
    left: 38px;
    top: 26px;
    margin: 0;
    font-size: 16.5px;
    font-weight: 600;
    letter-spacing: 0.1px;
    color: var(--brand-navy);
    line-height: 1;
  }
  .holder-name .surname { color: var(--brand-sky); }
  .holder-title {
    position: absolute;
    left: 39px;
    top: 46px;
    margin: 0;
    font-size: 12.5px;
    color: var(--ink);
    line-height: 1;
  }
  .brand-lockup {
    position: absolute;
    left: 184px;
    top: 77px;
    display: flex;
    align-items: center;
    gap: 10px;
  }
  .brand-dot {
    width: 62px;
    height: 62px;
    border-radius: 50%;
    background: var(--brand-sky);
  }
  .brand-name {
    font-size: 38px;
    font-weight: 700;
    color: var(--brand-navy);
    letter-spacing: -0.5px;
    line-height: 1;
  }
  .brand-tagline {
    position: absolute;
    left: 214px;
    top: 153px;
    margin: 0;
    font-size: 12.5px;
    font-weight: 600;
    color: var(--brand-sky);
    line-height: 1;
    letter-spacing: 0.1px;
  }
  .contact-list {
    position: absolute;
    left: 28px;
    top: 184px;
    margin: 0;
    padding: 0;
    list-style: none;
  }
  .contact-list li {
    display: flex;
    align-items: center;
    gap: 5px;
    height: 16px;
    font-size: 12.5px;
    color: var(--ink);
  }
  .contact-icon {
    width: 11px;
    height: 11px;
    flex: none;
  }
  .back-pattern {
    position: absolute;
    inset: 0;
    background: radial-gradient(circle at 50% 50%, var(--brand-sky-soft) 0%, var(--brand-sky-back) 70%);
  }
  .back-name {
    position: absolute;
    left: 0;
    right: 0;
    top: 100px;
    margin: 0;
    text-align: center;
    font-size: 64px;
    font-weight: 700;
    color: var(--brand-navy);
    letter-spacing: -1px;
    line-height: 1;
  }
</style>
</head>
<body>
<main class="stage">

  <section class="card card-front" aria-label="Business card front">
    <svg class="card-shapes" width="440" height="271" viewBox="0 0 440 271" aria-hidden="true">
      <polygon class="corner-tab-light" points="0,27 10,27 16,63 0,63" fill="var(--brand-sky)"/>
      <polygon class="corner-tab-dark" points="12,27 28,27 28,63 18,63" fill="var(--brand-navy)"/>
      <rect class="footer-band-light" x="0" y="257" width="215" height="14" fill="var(--brand-sky)"/>
      <polygon class="footer-band-dark" points="227,252 440,252 440,271 208,271" fill="var(--brand-navy)"/>
    </svg>

    <h1 class="holder-name">DANIEL <span class="surname">HARPER</span></h1>
    <p class="holder-title">Managing Director</p>

    <div class="brand-lockup">
      <span class="brand-dot" aria-hidden="true"></span>
      <span class="brand-name">PRAMORA</span>
    </div>
    <p class="brand-tagline">WHERE DOORS OPEN WIDE</p>

    <ul class="contact-list">
      <li>
        <svg class="contact-icon" viewBox="0 0 12 12" aria-hidden="true">
          <path d="M1 4 Q6 0 11 4 L9.5 5.5 L8 4.5 L8 3.5 Q6 3 4 3.5 L4 4.5 L2.5 5.5 Z" fill="var(--brand-navy)"/>
          <rect x="2.5" y="6" width="7" height="5" rx="1" fill="var(--brand-navy)"/>
        </svg>
        <span>02-9471 3385</span>
      </li>
      <li>
        <svg class="contact-icon" viewBox="0 0 12 12" aria-hidden="true">
          <rect x="3" y="0.5" width="6" height="11" rx="1.2" fill="none" stroke="var(--brand-navy)" stroke-width="1.3"/>
          <circle cx="6" cy="9.3" r="0.7" fill="var(--brand-navy)"/>
        </svg>
        <span>0412 608 274</span>
      </li>
      <li>
        <svg class="contact-icon" viewBox="0 0 12 12" aria-hidden="true">
          <rect x="1" y="2.5" width="10" height="7" fill="var(--brand-navy)"/>
          <polyline points="1,2.5 6,6.5 11,2.5" fill="none" stroke="#ffffff" stroke-width="1"/>
        </svg>
        <span>hello@pramora.au</span>
      </li>
    </ul>
  </section>

  <section class="card card-back" aria-label="Business card back">
    <div class="back-pattern" role="img" aria-label="Repeating pattern of the brand symbol in soft blue"></div>
    <p class="back-name">PRAMORA</p>
  </section>

</main>
</body>
</html>
```